New exciting tequila brand needs fun and attention drawing bottle label.

We need a design for on the glass bottle for a new tequila brand called "Mango Spin Tequila". It can be a label, or the decoration for the entire bottle.
The brand is called "Mango Spin" and is targeting a young party crowd.
I would like the visual to play with the image of a "tiger" & the idea of "up"side down.
In a bar the bottle needs to stand out, so it can be a very colourful design.

Good luck

Target Market(s)

young party crowd

Industry/Entity Type

Crowd

Colors
ec2027
fbed22
f37123
ffffff
f8ba93
fbf289

Requirements
Must have
• tiger
Nice to have
• play with the idea of upside down
Should not have
• have seen it before feeling

```html
<!DOCTYPE html>
<html lang="en">
<head>
<meta charset="utf-8">
<title>Mango Spin Tequila – Bottle Label</title>
<link rel="stylesheet" href="https://fonts.googleapis.com/css2?family=Teko:wght@500;600&family=Oswald:wght@500&display=swap">
<style>
  :root {
    --canvas-bg: #f2f2f2;
    --label-yellow: #fbf800;
    --ink-black: #111111;
    --tiger-red: #ec2027;
    --tiger-orange: #f37123;
  }
  * { margin: 0; padding: 0; box-sizing: border-box; }
  html, body {
    width: 1200px;
    height: 1000px;
    overflow: hidden;
    background: var(--canvas-bg);
  }
  .canvas {
    position: relative;
    width: 1200px;
    height: 1000px;
  }
  .label {
    position: absolute;
    left: 366px;
    top: 42px;
    width: 468px;
    height: 917px;
    background: var(--label-yellow);
    border-radius: 50% 50% 0 0 / 48px 48px 0 0;
    overflow: hidden;
    color: var(--ink-black);
    font-family: "Teko", "Oswald", sans-serif;
    font-weight: 600;
  }
  .brand-name {
    position: absolute;
    top: 62px;
    left: 0;
    width: 100%;
    text-align: center;
    text-transform: uppercase;
    line-height: 0.8;
    white-space: nowrap;
    font-weight: 600;
  }
  .brand-name .line-one {
    display: block;
    font-size: 118px;
    letter-spacing: 1px;
  }
  .brand-name .line-two {
    display: block;
    font-size: 128px;
    margin-top: 10px;
  }
  .tiger-emblem {
    position: absolute;
    left: 0;
    top: 282px;
    width: 100%;
    height: 340px;
    background: radial-gradient(ellipse at 50% 50%, var(--tiger-orange) 0%, var(--tiger-red) 55%, var(--label-yellow) 72%);
  }
  .product-type {
    position: absolute;
    top: 648px;
    left: 0;
    width: 100%;
    text-align: center;
    font-size: 128px;
    line-height: 1;
    text-transform: uppercase;
    white-space: nowrap;
    transform: rotate(180deg);
    letter-spacing: 1px;
  }
  .label-footer {
    position: absolute;
    left: 34px;
    right: 34px;
    top: 838px;
    display: flex;
    align-items: center;
    justify-content: space-between;
  }
  .label-footer .abv,
  .label-footer .volume {
    font-size: 44px;
    line-height: 1;
  }
  .label-footer .legal {
    font-family: "Oswald", sans-serif;
    font-weight: 500;
    font-size: 14px;
    line-height: 1.15;
    text-transform: uppercase;
    margin-right: 40px;
  }
</style>
</head>
<body>
  <main class="canvas">
    <section class="label">
      <h1 class="brand-name">
        <span class="line-one">Mango</span>
        <span class="line-two">Spin</span>
      </h1>
      <div class="tiger-emblem" role="img" aria-label="Geometric red line-art tiger head with whiskers spanning the label"></div>
      <p class="product-type">Tequila</p>
      <footer class="label-footer">
        <span class="abv">40%</span>
        <span class="legal">Product of Mexico<br>Enjoy responsibly</span>
        <span class="volume">70cl</span>
      </footer>
    </section>
  </main>
</body>
</html>
```